Brightward Rising Coaching Website

I specialize in instilling a profound sense of self-confidence and elevating self-esteem. Through tailored coaching, I help individuals overcome self-doubt, rewrite negative narratives, and embrace their unique strengths. With my support, you will navigate challenges with newfound resilience and develop an unshakable belief in your abilities.

One of my core focuses is equipping you with the tools to manage the delicate dance between work and life. Striking a harmonious work-life balance is essential for overall well-being, and I provide practical strategies to help you thrive in both realms. My approach nurtures your holistic development, allowing you to achieve professional success without compromising your personal happiness.

As a Motivational Speaker, I bring dynamic energy and thought-provoking insights to inspire positive change. I share the transformative power of cultivating a positive mindset, offering strategies to shift perspectives and embrace challenges as opportunities for growth.

Your journey towards improved mental health and overall well-being is at the heart of my coaching and speaking engagements. I am dedicated to providing you with actionable tools that promote mental clarity, emotional resilience, and a sense of inner peace. Through this process, you will develop the skills to overcome obstacles, manage stress, and foster a life of fulfillment.

Let's embark on this journey together. With my guidance, you'll empower yourself with the mindset, tools, and strategies needed to navigate life's complexities, elevate your self-esteem, and cultivate a life of balanced success and well-being. It's time to step into your greatness and achieve the life you deserve.

Target Market(s)
Women who want to improve their self-esteem and manage work-life balance

Industry/Entity Type
Motivational Coaching

Target Market(s)

Women who want to elevate their self-esteem and effectively navigate through work life balance.

Industry/Entity Type

Coaching

Coding

Font styles to use
Other font styles liked:
• Ariel , Script, or Serif used strategically throughout

Colors
59FF00
82FF00
B8FF75
E3FFCB
F4FFEA
FFF300
FFF600
FEFA6F
FFFEC7
FFFEE8
6B429C
8869AF
B7A5CE
E3DAEB
F3F0F8

Requirements
Must have
• About Me page, Coaching, Speaking, Frequently Asked Questions, Book an inquiry call, work with Dr. Marisol, pay in full, pay in payments,
Nice to have
• See https://www.velmorquade.example/home/#speaking - I would like sections similar to this website. A diversity of women of all ethnicities to include in business attire and leisure/fun attire, some happy pictures, some fun activities
Should not have
• Pictures of men

```html
<!DOCTYPE html>
<html lang="en">
<head>
<meta charset="utf-8">
<title>Brightward Rising Coaching</title>
<link href="https://fonts.googleapis.com/css2?family=Open+Sans:wght@400;600;700&family=Tinos:wght@400;700&display=swap" rel="stylesheet">
<style>
:root{
  --purple:#8869af;
  --purple-deep:#6b429c;
  --lav:#b7a5ce;
  --lav-soft:#e3daeb;
  --lav-pale:#f3f0f8;
  --blue:#4fc3e8;
  --ink:#333;
  --muted:#777;
  --dark:#2b2e38;
  --white:#fff;
}
*{margin:0;padding:0;box-sizing:border-box}
html,body{width:1200px;height:4544px;overflow:hidden}
body{position:relative;font-family:"Open Sans",Arial,sans-serif;color:var(--ink);background:var(--white)}
.abs{position:absolute}
.serif{font-family:"Tinos","Times New Roman",serif}
.grad-btn{background:linear-gradient(90deg,var(--blue),var(--lav));color:#fff;font-weight:700;border-radius:22px;display:flex;align-items:center;justify-content:center}
/* header */
.site-header{top:0;left:0;width:1200px;height:124px;background:#fff;z-index:5}
.contact-mini{top:20px;display:flex;gap:12px;align-items:center;font-size:11px;line-height:15px}
.contact-mini .dot{width:28px;height:28px;border-radius:50%;background:linear-gradient(135deg,var(--blue),var(--lav));display:flex;align-items:center;justify-content:center}
.contact-mini b{display:block;font-size:11px;color:#222}
.contact-mini span{color:#666;font-size:10px}
.nav-line{top:68px;height:1px;background:#ddd}
.nav{top:88px;font-size:12px;color:#555}
.logo-tab{top:0;left:500px;width:200px;height:146px;background:#fff;border-radius:0 0 30px 30px;z-index:6}
.logo-ring{top:16px;left:542px;width:116px;height:116px;border-radius:50%;border:2px solid var(--purple);display:flex;align-items:center;justify-content:center;text-align:center;z-index:7;font-family:"Tinos",serif;font-weight:700;color:var(--purple);font-size:17px;line-height:19px}
.book-btn{top:14px;left:880px;width:182px;height:39px;font-size:11px;font-weight:600}
/* hero */
.hero{top:124px;left:0;width:1200px;height:723px;overflow:hidden}
.hero-photo{position:absolute;inset:0;background:linear-gradient(100deg,#1f1b1a 0%,#3a3330 45%,#6a5a4f 70%,#3b322d 100%)}
.eyebrow{left:83px;color:#fff;font-size:19px;letter-spacing:6px;font-weight:700}
.hero h1{left:78px;color:#fff;font-size:50px;font-weight:600;letter-spacing:.5px}
.hero-rule{left:83px;width:649px;height:2px;background:#fff}
.hero-copy{left:83px;width:620px;color:#fff;font-size:15px;line-height:28px}
.btn-learn{left:83px;width:146px;height:39px;font-size:14px}
.btn-quote{left:240px;width:180px;height:39px;border-radius:22px;background:#fff;color:var(--purple-deep);font-weight:700;font-size:14px;display:flex;align-items:center;justify-content:center}
/* about */
.about-ring{top:966px;left:106px;width:440px;height:440px;border-radius:50%;border:2px solid #2f8fbf}
.about-photo{top:978px;left:118px;width:416px;height:416px;border-radius:50%;background:linear-gradient(135deg,#5a6d86,#b8a79b 55%,#2f3744)}
.about-badge{top:1218px;left:367px;width:194px;height:194px;border-radius:50%;background:linear-gradient(135deg,#3a3a44,#1e1f26);display:flex;align-items:center;justify-content:center;text-align:center;color:#fff;font-family:"Tinos",serif;font-weight:700;font-size:17px;line-height:20px}
.about-kicker{top:976px;left:621px;color:var(--purple);font-size:17px}
.about h2{top:1012px;left:621px;font-size:39px;font-weight:400;color:#222}
.about-quote{top:1078px;left:621px;width:460px;height:64px;border-left:2px solid var(--lav);padding:10px 0 0 15px;font-size:13px;line-height:23px;color:#777}
.about-copy{left:621px;width:470px;font-size:13px;line-height:23.5px;color:#666}
.btn-contact{top:1359px;left:620px;width:139px;height:44px;border-radius:0 22px 0 0;font-size:15px}
/* services */
.services{top:1511px;left:0;width:1200px;height:572px;background:var(--lav-pale)}
.sec-title{width:1200px;text-align:center;font-family:"Tinos",serif;color:var(--purple);font-size:46px;font-weight:400}
.sec-sub{width:1200px;text-align:center;font-size:13px;line-height:24px;color:#777}
.svc-card{top:1749px;width:319px;height:267px;border-radius:6px;overflow:hidden}
.svc-card .fill{position:absolute;inset:0}
.svc-card h3{position:absolute;top:64px;left:28px;color:#fff;font-family:"Tinos",serif;font-size:29px;font-weight:700}
.svc-card svg.arrow{position:absolute;left:42px;top:210px}
.svc-icon{top:1714px;width:70px;height:70px;border-radius:50%;background:#fff;display:flex;align-items:center;justify-content:center;box-shadow:0 2px 6px rgba(0,0,0,.08);z-index:2}
/* why */
.blob-left{top:2320px;left:120px;width:430px;height:428px;border-radius:214px;background:linear-gradient(90deg,rgba(243,240,248,0),var(--lav-soft))}
.blob-right{top:2320px;left:650px;width:430px;height:428px;border-radius:214px;background:linear-gradient(270deg,rgba(243,240,248,0),var(--lav-soft))}
.why-circle{top:2410px;left:460px;width:280px;height:290px;border-radius:50%;background:var(--lav)}
.why-photo{top:2292px;left:478px;width:244px;height:408px;border-radius:110px 110px 122px 122px;background:linear-gradient(180deg,#d9c5b0 0%,#b89276 28%,#3a3434 55%,#1a1a1d 100%)}
.feat-icon{width:88px;height:88px;border-radius:50%;background:var(--purple);border:4px solid #fff;box-shadow:0 0 0 2px var(--lav);display:flex;align-items:center;justify-content:center;z-index:3}
.feat h4{font-family:"Tinos",serif;font-weight:400;color:var(--purple);font-size:22px;white-space:nowrap}
.feat p{font-size:13px;line-height:24px;color:#888;margin-top:8px}
.feat.left{text-align:right;left:100px;width:278px}
.feat.right{left:796px;width:300px}
/* appointment */
.appt{top:2838px;left:0;width:1200px;height:563px;background:linear-gradient(90deg,#24262c,#3c3e44 50%,#2a2c31)}
.hours h3{top:2974px;left:94px;font-family:"Tinos",serif;font-size:27px;color:#fff;font-weight:400}
.hours-table{top:3036px;left:97px;width:489px;height:235px;border-left:3px solid var(--purple);background:rgba(0,0,0,.25)}
.hours-row{position:absolute;left:35px;right:35px;display:flex;justify-content:space-between;font-size:15px;color:#ddd;border-bottom:1px solid rgba(255,255,255,.08);padding-bottom:14px}
.hours-row b{font-weight:600;color:#fff}
.form-panel{top:2868px;left:611px;width:492px;height:498px;background:var(--lav-soft)}
.field{position:absolute;height:53px;background:#fff;font-size:14px;color:#333;padding-left:28px;display:flex;align-items:center}
.submit{top:3292px;left:665px;width:385px;height:53px;background:var(--purple);color:#fff;font-weight:700;font-size:19px;display:flex;align-items:center;justify-content:center}
/* reviews */
.reviews{top:3401px;left:0;width:1200px;height:620px;background:linear-gradient(180deg,var(--lav-pale),#f1edf7)}
.rev-card{top:3680px;width:321px;height:265px;background:#fff;padding:0 27px;box-shadow:0 2px 10px rgba(0,0,0,.04)}
.rev-card .stars{margin-top:56px;color:#f07a20;font-size:15px;letter-spacing:3px}
.rev-card p{font-size:12.5px;line-height:24px;color:#777;margin-top:6px}
.rev-card h5{font-family:"Tinos",serif;font-weight:400;font-size:20px;color:#222;margin-top:14px}
.rev-card small{font-size:9px;color:var(--purple);font-weight:600;letter-spacing:.3px}
.avatar{top:3645px;width:64px;height:64px;border-radius:50%;border:3px solid #fff;box-shadow:0 1px 4px rgba(0,0,0,.15);background:linear-gradient(135deg,#d8c6b6,#7a6656);z-index:2}
.quote-mark{top:3650px;font-family:"Tinos",serif;font-size:100px;color:var(--lav);line-height:1;font-weight:700;z-index:2}
/* footer */
.footer-nav{top:4306px;left:0;width:1200px;display:flex;justify-content:center;gap:48px;color:#fff;font-size:14px}
.foot-rule{top:4360px;left:141px;width:918px;height:1px;background:rgba(255,255,255,.25)}
.foot-contact{top:4405px;display:flex;align-items:center;gap:16px;color:#fff;font-size:12px;line-height:17px}
.foot-contact .ic{width:54px;height:54px;border-radius:50%;border:1.5px solid #fff;display:flex;align-items:center;justify-content:center}
.foot-div{top:4400px;width:1px;height:64px;background:rgba(255,255,255,.3)}
.bottom-bar{top:4488px;left:0;width:1200px;height:56px;background:linear-gradient(90deg,var(--blue),var(--lav))}
.social{top:4505px;width:26px;height:26px;border:1px solid rgba(255,255,255,.8);border-radius:3px}
</style>
</head>
<body>

<!-- HEADER -->
<header class="abs site-header">
  <div class="abs contact-mini" style="left:125px">
    <div class="dot"><svg width="14" height="14" viewBox="0 0 24 24"><path d="M6.6 10.8a15 15 0 006.6 6.6l2.2-2.2c.3-.3.7-.4 1-.2 1.1.4 2.3.6 3.6.6.6 0 1 .4 1 1V20c0 .6-.4 1-1 1A17 17 0 013 4c0-.6.4-1 1-1h3.5c.6 0 1 .4 1 1 0 1.3.2 2.5.6 3.6.1.3 0 .7-.2 1z" fill="#fff"/></svg></div>
    <div><b>Call Us:</b><span>(555) 010-4432</span></div>
  </div>
  <div class="abs contact-mini" style="left:281px">
    <div class="dot"><svg width="14" height="12" viewBox="0 0 24 18"><rect x="1" y="1" width="22" height="16" rx="2" fill="none" stroke="#fff" stroke-width="2"/><path d="M1 2l11 8 11-8" fill="none" stroke="#fff" stroke-width="2"/></svg></div>
    <div><b>Email:</b><span>office@brightward.example</span></div>
  </div>
  <div class="abs nav-line" style="left:120px;width:365px"></div>
  <div class="abs nav-line" style="left:700px;width:365px"></div>
  <nav>
    <span class="abs nav" style="left:126px">Home</span>
    <span class="abs nav" style="left:238px">About Us</span>
    <span class="abs nav" style="left:388px">Services</span>
    <span class="abs nav" style="left:707px">Coaching</span>
    <span class="abs nav" style="left:834px">Speaking</span>
    <span class="abs nav" style="left:958px">Contact Us</span>
  </nav>
  <div class="abs grad-btn book-btn">BOOK APPOINTMENT</div>
</header>
<div class="abs logo-tab"></div>
<div class="abs logo-ring">Brightward<br>Rising</div>

<!-- HERO -->
<section class="abs hero">
  <div class="hero-photo" role="img" aria-label="Photo of a woman speaking at a lectern to a seated audience"></div>
  <div class="abs eyebrow" style="top:204px">BRIGHTWARD RISING</div>
  <h1 class="abs" style="top:248px">Rise Above, Inspire Beyond</h1>
  <div class="abs hero-rule" style="top:333px"></div>
  <p class="abs hero-copy" style="top:363px">Lorem ipsum dolor sit amet, consectetur adipiscing elit, sed do eiusmod tempor incididunt ut labore et dolore magna</p>
  <div class="abs grad-btn btn-learn" style="top:451px">LEARN MORE</div>
  <div class="abs btn-quote" style="top:451px">REQUEST QUOTE</div>
  <svg class="abs" style="left:0;top:0" width="1200" height="723" viewBox="0 0 1200 723">
    <defs>
      <linearGradient id="wv" x1="0" x2="1"><stop offset="0" stop-color="#4fc3e8"/><stop offset=".5" stop-color="#b7a5ce"/><stop offset="1" stop-color="#4fc3e8"/></linearGradient>
    </defs>
    <path d="M0 570 Q560 760 1200 570 L1200 600 Q600 780 0 610Z" fill="url(#wv)"/>
    <path d="M0 600 Q520 790 1200 595 L1200 723 L0 723Z" fill="#fff"/>
  </svg>
</section>

<!-- ABOUT -->
<section class="about">
  <div class="abs about-ring"></div>
  <div class="abs about-photo" role="img" aria-label="Photo of a coach presenting to a group of women"></div>
  <div class="abs about-badge">Brightward<br>Rising</div>
  <div class="abs about-kicker serif">Dare to Dream Big</div>
  <h2 class="abs serif">Believe, Achieve, Succeed.</h2>
  <div class="abs about-quote">Lorem ipsum dolor sit amet, consectetur adipiscing elit, sed do eiusmod or incididunt ut labore et dolore</div>
  <p class="abs about-copy" style="top:1162px">Lorem ipsum dolor sit amet, consectetur adipiscing elit, sed do eiusmod obgr incididunt ut labore et dolore Lorem ipsum dolor sit amet, consectetur adip iscing elit, sed do eiusmod tempor incididunt ut labore et dolore m agna aliqua. Ut enim ad minim veniam, quis nostrud exercitation ullamco laboris nisi ut aliquip ex ea commodo consequat.</p>
  <p class="abs about-copy" style="top:1294px">Lorem ipsum dolor sit amet, consectetur adipiscing elit, sed do eiusmod obgr incididunt ut labore et dolore Lorem ipsum dol</p>
  <div class="abs grad-btn btn-contact">Contact us</div>
</section>

<!-- SERVICES -->
<section class="abs services"></section>
<h2 class="abs sec-title" style="top:1560px;left:0">Our Services</h2>
<p class="abs sec-sub" style="top:1627px;left:0">Lorem ipsum dolor sit amet, consectetur adipiscing elit, sed do eiusmod temp<br>or incididunt ut labore et dolore</p>

<div class="abs svc-card" style="left:92px">
  <div class="fill" role="img" aria-label="Photo of smiling women standing together" style="background:linear-gradient(135deg,#6f6a66,#b9a995 50%,#5d5650)"></div>
  <h3>Keynote Speaches</h3>
  <svg class="arrow" width="46" height="14" viewBox="0 0 46 14"><path d="M0 7h44M37 1l7 6-7 6" fill="none" stroke="#fff" stroke-width="1.5"/></svg>
</div>
<div class="abs svc-card" style="left:440px">
  <div class="fill" role="img" aria-label="Photo of a woman consulting with a laptop in an office" style="background:linear-gradient(135deg,#4b4c52,#8f8a86 55%,#2f3034)"></div>
  <h3>Consulting</h3>
  <svg class="arrow" width="46" height="14" viewBox="0 0 46 14"><path d="M0 7h44M37 1l7 6-7 6" fill="none" stroke="#fff" stroke-width="1.5"/></svg>
</div>
<div class="abs svc-card" style="left:787px">
  <div class="fill" role="img" aria-label="Photo of friends hugging outdoors at sunset" style="background:linear-gradient(135deg,#3c3446,#a8784a 55%,#2d2630)"></div>
  <h3>Team Building</h3>
  <svg class="arrow" width="46" height="14" viewBox="0 0 46 14"><path d="M0 7h44M37 1l7 6-7 6" fill="none" stroke="#fff" stroke-width="1.5"/></svg>
</div>
<div class="abs svc-icon" style="left:138px"><svg width="30" height="30" viewBox="0 0 30 30" fill="none" stroke="#8aa6d6" stroke-width="1.6"><circle cx="14" cy="7" r="4"/><path d="M14 11l-2 9h8M5 25h20M8 25l3-8"/></svg></div>
<div class="abs svc-icon" style="left:486px"><svg width="30" height="30" viewBox="0 0 30 30" fill="none" stroke="#6aa6d6" stroke-width="1.8"><path d="M4 21a11 11 0 1122 0"/><path d="M15 21l6-7"/><circle cx="15" cy="21" r="1.5"/></svg></div>
<div class="abs svc-icon" style="left:833px"><svg width="30" height="30" viewBox="0 0 30 30" fill="none" stroke="#8ab4e0" stroke-width="1.8"><path d="M24 11a10 10 0 00-17-3M6 19a10 10 0 0017 3"/><path d="M7 3v5h5M23 27v-5h-5"/><circle cx="15" cy="15" r="3"/></svg></div>

<!-- WHY CHOOSE US -->
<h2 class="abs sec-title" style="top:2137px;left:0">Why Choose Us</h2>
<p class="abs sec-sub" style="top:2204px;left:0">Lorem ipsum dolor sit amet, consectetur adipiscing elit, sed do eiusmod temp<br>or incididunt ut labore et dolore</p>
<div class="abs blob-left"></div>
<div class="abs blob-right"></div>
<div class="abs why-circle"></div>
<div class="abs why-photo" role="img" aria-label="Photo of a smiling businesswoman with arms crossed"></div>

<div class="abs feat left" style="top:2360px"><h4>Variety of Classes</h4><p>Lorem ipsum dolor sit amet, conser adi<br>or incididunt ut labore et dolore</p></div>
<div class="abs feat left" style="top:2492px"><h4>Certified Instructors</h4><p>Lorem ipsum dolor sit amet, conser adi<br>or incididunt ut labore et dolore</p></div>
<div class="abs feat left" style="top:2626px"><h4>Personalized Approach</h4><p>Lorem ipsum dolor sit amet, conser adi<br>or incididunt ut labore et dolore</p></div>
<div class="abs feat right" style="top:2360px"><h4>Mind-Body Connection</h4><p>Lorem ipsum dolor sit amet, conser adi<br>or incididunt ut labore et dolore</p></div>
<div class="abs feat right" style="top:2492px"><h4>Flexible Schedule</h4><p>Lorem ipsum dolor sit amet, conser adi<br>or incididunt ut labore et dolore</p></div>
<div class="abs feat right" style="top:2626px"><h4>Specialized Workshops</h4><p>Lorem ipsum dolor sit amet, conser adi<br>or incididunt ut labore et dolore</p></div>

<div class="abs feat-icon" style="top:2358px;left:395px"><svg width="38" height="38" viewBox="0 0 30 30" fill="none" stroke="#fff" stroke-width="1.6"><circle cx="14" cy="7" r="4"/><path d="M14 11l-2 9h8M5 25h20M8 25l3-8"/></svg></div>
<div class="abs feat-icon" style="top:2491px;left:395px"><svg width="38" height="38" viewBox="0 0 30 30" fill="none" stroke="#fff" stroke-width="1.8"><path d="M4 21a11 11 0 1122 0"/><path d="M15 21l6-7"/></svg></div>
<div class="abs feat-icon" style="top:2625px;left:395px"><svg width="38" height="38" viewBox="0 0 30 30" fill="none" stroke="#fff" stroke-width="1.8"><path d="M24 11a10 10 0 00-17-3M6 19a10 10 0 0017 3"/><path d="M7 3v5h5M23 27v-5h-5"/></svg></div>
<div class="abs feat-icon" style="top:2358px;left:690px"><svg width="38" height="38" viewBox="0 0 30 30" fill="none" stroke="#fff" stroke-width="1.6"><circle cx="14" cy="7" r="4"/><path d="M14 11l-2 9h8M5 25h20M8 25l3-8"/></svg></div>
<div class="abs feat-icon" style="top:2491px;left:690px"><svg width="38" height="38" viewBox="0 0 30 30" fill="none" stroke="#fff" stroke-width="1.8"><path d="M4 21a11 11 0 1122 0"/><path d="M15 21l6-7"/></svg></div>
<div class="abs feat-icon" style="top:2625px;left:690px"><svg width="38" height="38" viewBox="0 0 30 30" fill="none" stroke="#fff" stroke-width="1.8"><path d="M24 11a10 10 0 00-17-3M6 19a10 10 0 0017 3"/><path d="M7 3v5h5M23 27v-5h-5"/></svg></div>

<!-- APPOINTMENT -->
<section class="abs appt" role="img" aria-label="Dimmed photo of women laughing together at a table"></section>
<div class="hours">
  <h3 class="abs">Opening Hours</h3>
  <div class="abs hours-table">
    <div class="hours-row" style="top:28px"><b>Monday - Thursday</b><span>08am - 05pm</span></div>
    <div class="hours-row" style="top:79px"><b>Saturday</b><span>08am - 02pm</span></div>
    <div class="hours-row" style="top:130px"><b>Phone</b><span>+123 456 7890</span></div>
    <div class="hours-row" style="top:181px;border-bottom:none"><b>Email</b><span>info@company.com</span></div>
  </div>
</div>
<div class="abs form-panel"></div>
<div class="abs" style="top:2906px;left:664px;width:56px;height:56px;border-radius:50%;background:var(--purple);display:flex;align-items:center;justify-content:center"><svg width="24" height="24" viewBox="0 0 24 24" fill="none" stroke="#fff" stroke-width="1.6"><rect x="3" y="5" width="18" height="15" rx="2"/><path d="M3 10h18M8 3v4M16 3v4"/></svg></div>
<div class="abs" style="top:2902px;left:733px;font-size:13px;color:#444">Get in touch with us any day any time</div>
<div class="abs serif" style="top:2923px;left:733px;font-size:34px;color:#222">Make Appointment</div>
<div class="field" style="top:3000px;left:665px;width:182px">First Name</div>
<div class="field" style="top:3000px;left:866px;width:184px">Last Name</div>
<div class="field" style="top:3073px;left:665px;width:182px">Email Address</div>
<div class="field" style="top:3073px;left:866px;width:184px">Phone Number</div>
<div class="field" style="top:3145px;left:665px;width:385px">Select Subject</div>
<div class="field" style="top:3219px;left:665px;width:385px">dd/mm/yyyy</div>
<div class="abs submit">SUBMIT</div>

<!-- REVIEWS -->
<section class="abs reviews"></section>
<h2 class="abs sec-title" style="top:3482px;left:0">Clients Review</h2>
<p class="abs sec-sub" style="top:3549px;left:0">Lorem ipsum dolor sit amet, consectetur adipiscing elit, sed do eiusmod temp<br>or incididunt ut labore et dolore</p>

<div class="abs rev-card" style="left:101px"><div class="stars">★★★★★</div><p>Lorem ipsum dolor sit amet, consectetur adipiscing elit, sed do eiusmod or incididun t ut labore et dolore Lorem ipsum dolor sit adipiscing elit, sed do ehjhj</p><h5>Tara Wendel</h5><small>BUSINESSMAN</small></div>
<div class="abs rev-card" style="left:445px;border-bottom:4px solid;border-image:linear-gradient(90deg,var(--blue),var(--lav)) 1"><div class="stars">★★★★★</div><p>Lorem ipsum dolor sit amet, consectetur adipiscing elit, sed do eiusmod or incididun t ut labore et dolore Lorem ipsum dolor sit adipiscing elit, sed do ehjhj</p><h5>Tara Wendel</h5><small>BUSINESSMAN</small></div>
<div class="abs rev-card" style="left:787px"><div class="stars">★★★★★</div><p>Lorem ipsum dolor sit amet, consectetur adipiscing elit, sed do eiusmod or incididun t ut labore et dolore Lorem ipsum dolor sit adipiscing elit, sed do ehjhj</p><h5>Tara Wendel</h5><small>BUSINESSMAN</small></div>
<div class="abs avatar" style="left:132px" role="img" aria-label="Client portrait"></div>
<div class="abs avatar" style="left:476px" role="img" aria-label="Client portrait"></div>
<div class="abs avatar" style="left:818px" role="img" aria-label="Client portrait"></div>
<div class="abs quote-mark" style="left:330px">”</div>
<div class="abs quote-mark" style="left:673px;color:var(--purple)">”</div>
<div class="abs quote-mark" style="left:1015px">”</div>

<!-- FOOTER -->
<svg class="abs" style="top:3960px;left:0" width="1200" height="528" viewBox="0 0 1200 528">
  <defs><linearGradient id="fl" x1="0" x2="1"><stop offset="0" stop-color="#4fc3e8"/><stop offset=".5" stop-color="#b7a5ce"/><stop offset="1" stop-color="#8869af"/></linearGradient></defs>
  <path d="M0 10 Q600 170 1200 10 L1200 528 L0 528Z" fill="#2b2e38"/>
  <path d="M240 118 Q604 165 970 118" fill="none" stroke="url(#fl)" stroke-width="3"/>
  <circle cx="604" cy="138" r="30" fill="#fff"/>
  <circle cx="604" cy="138" r="20" fill="none" stroke="#b7a5ce" stroke-width="1.5"/>
</svg>
<div class="abs" style="top:4174px;left:542px;width:116px;height:116px;border-radius:50%;border:2px solid var(--purple);display:flex;align-items:center;justify-content:center;text-align:center;font-family:'Tinos',serif;font-weight:700;color:var(--lav);font-size:17px;line-height:19px">Brightward<br>Rising</div>
<nav class="abs footer-nav"><span>HOME</span><span>SERVICES</span><span>ABOUT US</span><span>TESTIMONIALS</span><span>BLOG</span></nav>
<div class="abs foot-rule"></div>
<div class="abs foot-contact" style="left:178px">
  <div class="ic"><svg width="26" height="26" viewBox="0 0 24 24" fill="none" stroke="#fff" stroke-width="1.4"><circle cx="12" cy="12" r="9"/><path d="M3 12h18M12 3c3 3 3 15 0 18M12 3c-3 3-3 15 0 18"/></svg></div>
  <div>123, Building Name, Street<br>City, State XY 123456</div>
</div>
<div class="abs foot-div" style="left:429px"></div>
<div class="abs foot-contact" style="left:510px">
  <div class="ic"><svg width="22" height="26" viewBox="0 0 20 26" fill="none" stroke="#fff" stroke-width="1.5"><rect x="4" y="2" width="12" height="22" rx="2"/><path d="M9 20h2"/></svg></div>
  <div>PHONE<br>(123) 456 7890</div>
</div>
<div class="abs foot-div" style="left:750px"></div>
<div class="abs foot-contact" style="left:834px">
  <div class="ic"><svg width="26" height="22" viewBox="0 0 24 20" fill="none" stroke="#fff" stroke-width="1.5"><rect x="2" y="3" width="20" height="14" rx="2"/><path d="M2 4l10 7 10-7"/></svg></div>
  <div>EMAIL<br>info@company.com</div>
</div>
<div class="abs bottom-bar"></div>
<div class="abs" style="top:4508px;left:146px;color:#fff;font-size:12px;font-weight:600">Brightward Rising</div>
<div class="abs social" style="left:933px"></div>
<div class="abs social" style="left:965px"></div>
<div class="abs social" style="left:998px"></div>
<div class="abs social" style="left:1031px"></div>

</body>
</html>
```